Flash Banner Ad for web advertising

We are a float centre in Auckland, New Zealand. Please see our website at www.quietdriftpod.co.nz for more info on us and what we provide

We need an HTML5 flash ad for various websites promoting our product that generates traffic onto our website.

Dimensions (W x H): 300x250 pixels
Max File Size: 80 kB
Format: HTML5

This banner needs to be brief (3-4 slides) and visual, with booking being the last slide. Should say that the product provides relaxation and other benefits as can be seen on home page of our site. Needs to be a summary as people do not look at banners for long.

Please use images attached or images from our site, please message if you need more resources:
https://www.filevaultex.com/sh/qtpkw31zbnvalx/BBKrtenoj5sLwHczmgUdy7Pk?dl=0

Target Market(s)

Stressed individuals who need a break from every day life.

Industry/Entity Type

Health And Wellness

Colors
3176b5
0592cd
34a7d8
add136
9bcb3c
33b8a4
ffffff

Requirements
Must have
• Slides that finish into a website book now link

```html
<!DOCTYPE html>
<html lang="en">
<head>
<meta charset="utf-8">
<title>Quiet Drift – banner sequence</title>
<link rel="stylesheet" href="https://fonts.googleapis.com/css2?family=Montserrat:wght@300;400;500&display=swap">
<style>
  :root {
    --page: #ffffff;
    --white: #ffffff;
    --space-deep: #0b1240;
    --space-mid: #1d3c8f;
    --space-glow: #9fc8ff;
    --float-dark: #15152b;
    --float-mid: #1f2350;
    --float-water: #2344a0;
    --float-shadow: #0a0f2e;
    --float-skin: rgba(170,140,130,0.28);
    --water-light: #34a7d8;
    --water-mid: #0592cd;
    --water-deep: #3176b5;
    --ring-outer: rgba(255,255,255,0.10);
    --ring-inner: rgba(255,255,255,0.16);
  }
  * { box-sizing: border-box; margin: 0; padding: 0; }
  html, body {
    width: 1200px; height: 191px; overflow: hidden;
    background: var(--page);
    font-family: "Montserrat", Arial, sans-serif;
    font-weight: 300;
    color: var(--white);
  }
  .strip {
    position: absolute; left: 12px; top: 14px;
    width: 1176px; height: 161px;
    display: flex;
  }
  .slide { position: relative; width: 196px; height: 161px; overflow: hidden; }
  .visual { position: absolute; inset: 0; }
  .visual--space {
    background:
      radial-gradient(ellipse 120% 38% at 50% 100%, var(--space-glow) 0%, #4f7fd8 25%, transparent 60%),
      radial-gradient(circle at 50% 30%, var(--space-mid) 0%, var(--space-deep) 75%);
  }
  .visual--floater {
    background:
      radial-gradient(ellipse 34% 22% at 76% 42%, var(--float-skin) 0%, transparent 100%),
      radial-gradient(ellipse 40% 30% at 10% 62%, rgba(120,100,110,0.22) 0%, transparent 100%),
      linear-gradient(90deg, var(--float-shadow) 0%, transparent 18%),
      linear-gradient(180deg, var(--float-dark) 0%, var(--float-mid) 45%, var(--float-water) 66%, var(--float-shadow) 82%, #142a70 100%);
  }
  .visual--water {
    background: linear-gradient(180deg, var(--water-deep) 0%, var(--water-mid) 25%, var(--water-light) 60%, var(--water-mid) 100%);
  }

  .headline { position: absolute; line-height: 1; white-space: nowrap; font-weight: 300; }

  .yoga { left: 36px; top: 40px; }
  .yoga .big { display: block; font-size: 36px; font-weight: 400; margin-left: 24px; }
  .yoga .small { display: block; font-size: 15px; line-height: 1.05; margin-top: 2px; }
  .yoga .small span { display: block; padding-left: 38px; }

  .word {
    left: 0; right: 0; top: 100px; text-align: center;
    font-size: 29px; letter-spacing: 0.3px;
  }

  .breathe { right: 46px; top: 44px; text-align: right; }
  .breathe .big { display: block; font-size: 27px; line-height: 0.95; }
  .breathe .small { display: block; font-size: 14px; margin-top: 5px; }

  .corner-name {
    position: absolute; right: 7px; bottom: 7px;
    font-size: 7px; font-weight: 400; letter-spacing: 0.3px;
  }

  .rings { position: absolute; left: 0; top: 0; }
  .brand-name {
    position: absolute; left: 0; right: 0; top: 72px; text-align: center;
    font-size: 14px; font-weight: 400;
  }
  .book-now {
    position: absolute; left: 0; right: 0; top: 132px; text-align: center;
    font-size: 8px; font-weight: 500; letter-spacing: 1px;
  }
  .url {
    position: absolute; left: 0; right: 0; top: 146px; text-align: center;
    font-size: 7.5px; font-weight: 400; letter-spacing: 0.4px;
    color: var(--white); text-decoration: none;
  }
</style>
</head>
<body>
  <main class="strip">
    <section class="slide">
      <div class="visual visual--space" role="img" aria-label="Starfield over a glowing planet horizon"></div>
      <h2 class="headline yoga"><span class="big">Yoga</span><span class="small">for your<span>mind</span></span></h2>
    </section>

    <section class="slide">
      <div class="visual visual--floater" role="img" aria-label="Person floating peacefully in a dark blue-lit pool"></div>
      <h2 class="headline word">DISCOVER</h2>
      <span class="corner-name">Quiet Drift</span>
    </section>

    <section class="slide">
      <div class="visual visual--floater" role="img" aria-label="Person floating peacefully in a dark blue-lit pool"></div>
      <h2 class="headline word">RELAX</h2>
      <span class="corner-name">Quiet Drift</span>
    </section>

    <section class="slide">
      <div class="visual visual--floater" role="img" aria-label="Person floating peacefully in a dark blue-lit pool"></div>
      <h2 class="headline word">RECOVER</h2>
      <span class="corner-name">Quiet Drift</span>
    </section>

    <section class="slide">
      <div class="visual visual--water" role="img" aria-label="Underwater view of rippling blue water surface"></div>
      <h2 class="headline breathe"><span class="big">Breathe<br>deep</span><span class="small">and let go...</span></h2>
      <span class="corner-name">Quiet Drift</span>
    </section>

    <section class="slide">
      <div class="visual visual--water" role="img" aria-label="Underwater view of rippling blue water surface"></div>
      <svg class="rings" width="196" height="161" aria-hidden="true">
        <circle cx="98" cy="78" r="70" fill="var(--ring-outer)"/>
        <circle cx="98" cy="78" r="52" fill="var(--ring-inner)"/>
      </svg>
      <p class="brand-name">Quiet Drift</p>
      <p class="book-now">BOOK NOW</p>
      <a class="url" href="https://www.quietdriftpod.co.nz">QUIETDRIFTPOD.CO.NZ</a>
    </section>
  </main>
</body>
</html>
```